Business Card Design Project

We need a redesign of our business card.
We are a Consulting Property Developer called The Kestrel Group
Updates

Thank you all for submissions. Just waiting on managment to decide.

Thank you,

Dorinda

Industry/Entity Type

Business

Requirements
Must have
• we like having the KG a focus in the back ground or on the side
Kestrel is our company colour

the wording - property development
and - premium accommodation

our website www.kestrelgroup-example.com.au

persons name
title

p: 1300 482917 f: 1300 482915 m: 0417593824
PO Box 5817, Brindlevale Qld 4178
e: admin@kestrelgroup-example.com.au

```html
<!DOCTYPE html>
<html lang="en">
<head>
<meta charset="utf-8">
<title>The Kestrel Group — Business Card</title>
<link rel="stylesheet" href="https://fonts.googleapis.com/css2?family=Open+Sans:ital,wght@1,400&family=Source+Sans+3:wght@400&display=swap">
<style>
  :root {
    --kestrel: #94193a;
    --ink: #1e1e1e;
    --rule-grey: #8c8c8c;
    --frame-grey: #858585;
    --band-blush: #f5ebee;
    --page: #ffffff;
  }
  html, body {
    margin: 0;
    width: 1200px;
    height: 900px;
    overflow: hidden;
    background: var(--page);
  }
  .stage {
    position: absolute;
    left: 0;
    top: 0;
    width: 1152px;
    height: 864px;
    transform: scale(1.0417);
    transform-origin: 0 0;
  }
  .card {
    position: absolute;
    left: 368px;
    top: 312px;
    width: 416px;
    height: 232px;
    box-sizing: border-box;
    border: 2px solid var(--frame-grey);
    background: var(--page);
    overflow: hidden;
  }
  .card__art {
    position: absolute;
    left: -2px;
    top: -2px;
    width: 416px;
    height: 232px;
  }
  .brand {
    position: absolute;
    left: 20px;
    top: 4px;
    display: flex;
    align-items: center;
    gap: 10px;
  }
  .brand__dot {
    width: 16px;
    height: 16px;
    border-radius: 50%;
    background: var(--kestrel);
  }
  .brand__name {
    font-family: "Source Sans 3", sans-serif;
    font-weight: 400;
    font-size: 34px;
    line-height: 40px;
    color: var(--kestrel);
    white-space: nowrap;
  }
  .tagline {
    position: absolute;
    font-family: "Source Sans 3", sans-serif;
    color: var(--kestrel);
    white-space: nowrap;
    margin: 0;
  }
  .tagline--primary { left: 112px; top: 46px; font-size: 16px; }
  .tagline--secondary { left: 103px; top: 65px; font-size: 12.5px; }
  .holder {
    position: absolute;
    right: 40px;
    top: 76px;
    text-align: right;
    font-family: "Open Sans", sans-serif;
    font-style: italic;
    font-size: 13.5px;
    line-height: 19px;
    color: var(--ink);
  }
  .holder p { margin: 0; }
  .contacts {
    position: absolute;
    left: 0;
    top: 174px;
    width: 416px;
    font-family: "Open Sans", sans-serif;
    font-style: italic;
    font-size: 11.5px;
    line-height: 15.5px;
    color: var(--ink);
  }
  .contacts__row { position: relative; height: 15.5px; white-space: nowrap; }
  .contacts__label, .contacts__value { position: absolute; top: 0; }
  .contacts__row:nth-child(1) .contacts__label { left: 81px; }
  .contacts__row:nth-child(1) .contacts__value { left: 196px; }
  .contacts__row:nth-child(2) .contacts__label { left: 78px; }
  .contacts__row:nth-child(2) .contacts__value { left: 193px; }
  .contacts__row:nth-child(3) .contacts__label { left: 74px; }
  .contacts__row:nth-child(3) .contacts__value { left: 188px; }
</style>
</head>
<body>
<main class="stage">
  <section class="card" aria-label="The Kestrel Group business card">
    <svg class="card__art" viewBox="0 0 416 232" aria-hidden="true">
      <polygon class="band" points="0,70 100,70 70,232 0,232" fill="var(--band-blush)"/>
      <line class="rule-logo" x1="18" y1="48" x2="372" y2="48" stroke="var(--rule-grey)" stroke-width="1"/>
      <polyline class="rule-accent" points="275,86 106,86 88,176" fill="none" stroke="var(--kestrel)" stroke-width="1.6"/>
      <polyline class="rule-grey" points="20,93 109,93 102,141" fill="none" stroke="var(--rule-grey)" stroke-width="1.6"/>
    </svg>

    <div class="brand">
      <span class="brand__dot"></span>
      <span class="brand__name">The Kestrel Group</span>
    </div>

    <p class="tagline tagline--primary">property development</p>
    <p class="tagline tagline--secondary">premium accommodation</p>

    <div class="holder">
      <p class="holder__name">persons name</p>
      <p class="holder__title">title</p>
    </div>

    <div class="contacts">
      <div class="contacts__row">
        <span class="contacts__label">p&nbsp;&nbsp;: 1300 482917</span>
        <span class="contacts__value">PO Box 5817</span>
      </div>
      <div class="contacts__row">
        <span class="contacts__label">f&nbsp;&nbsp;&nbsp;: 1300 482915</span>
        <span class="contacts__value">Brindlevale Qld 4178</span>
      </div>
      <div class="contacts__row">
        <span class="contacts__label">m : 0417593824</span>
        <span class="contacts__value">e: admin@kestrelgroup-example.com.au</span>
      </div>
    </div>
  </section>
</main>
</body>
</html>
```